Family Entertainment Center needs a fundraising flyer design

We need a 8.5 x 5.5 (half sheet of copy paper) flyer designed for a roller skating rink/family entertainment center in Wichita, KS. We partner with 100s of local schools each year by offering PTO fundraisers at our facility. With each party we send out flyers to the schools to send home with each kid to remind them of the time and date of the party as well as get them excited! Most of these schools and PTOs call these fundraisers "skate night".The information we need communicated or on our flyer is below:-Skating $6-Play Zone $6-Skate & Play $10-Skate Rental is included in above pricing-Price is per person-www.maplewheelrink.com-Maplewood Skate Center 847 S. Pinecrest Ave. Wichita, KS 67219-Our logo (attached)-The words or heading "Skate Night"-A blank, white space for us to print details in (see attached flyer for an example)

Target Market(s)

Elementary School parents and kids

Font styles to use
Serif
Sans Serif

Requirements
Must have
• The information outlined in the description and a blank white space incorporated into the design for our ability to print over.
Nice to have
• colors that match or compliment our logo, creative, but clean fonts

```html
<!DOCTYPE html>
<html lang="en">
<head>
<meta charset="utf-8">
<title>Skate Night Flyer</title>
<link rel="stylesheet" href="https://fonts.googleapis.com/css2?family=Kaushan+Script&family=Anton&family=Oswald:wght@700&family=Open+Sans:wght@400;700;800&family=Montserrat:wght@300;400&display=swap">
<style>
  :root {
    --navy: #0d1a5c;
    --royal: #1f36a0;
    --ray: #2a46b8;
    --red: #e41e26;
    --white: #ffffff;
    --ink: #111111;
    --yellow: #f7c21b;
    --cyan: #19b6ef;
    --magenta: #e5127d;
  }
  html, body { margin: 0; padding: 0; overflow: hidden; background: var(--white); }
  .flyer {
    position: relative; width: 927px; height: 1200px; overflow: hidden;
    background: var(--white); font-family: "Open Sans", sans-serif;
  }
  .art { position: absolute; inset: 0; z-index: 0; }
  .text { position: absolute; margin: 0; white-space: nowrap; z-index: 1; }
  .tagline {
    left: 34px; top: 120px; color: var(--white); font-weight: 800; font-size: 22px;
    line-height: 1; letter-spacing: 1px; transform: rotate(-15deg); transform-origin: left bottom;
  }
  .title-script {
    left: 135px; top: 222px; font-family: "Kaushan Script", cursive; font-weight: 400;
    font-size: 162px; color: var(--ink); line-height: 1;
  }
  .title-night {
    left: 420px; top: 421px; font-family: "Montserrat", sans-serif; font-weight: 300;
    font-size: 66px; color: var(--ink); line-height: 1;
  }
  .prices {
    left: 195px; width: 410px; text-align: center; color: var(--red);
    font-family: "Oswald", sans-serif; font-weight: 700; line-height: 1;
  }
  .prices--single { top: 534px; font-size: 37px; }
  .prices--bundle { top: 584px; font-size: 40px; }
  .price-note {
    left: 330px; width: 240px; top: 628px; text-align: center; color: var(--ink);
    font-size: 16px; line-height: 21px;
  }
  .brand-name {
    left: 690px; width: 168px; top: 463px; text-align: center; white-space: normal;
    color: var(--white); font-family: "Oswald", sans-serif; font-weight: 700;
    font-size: 22px; line-height: 26px; letter-spacing: 1px;
  }
  .promo-lead {
    left: 670px; top: 598px; color: var(--white); font-weight: 800; font-size: 25px;
    line-height: 1.2; z-index: 2;
  }
  .promo-main {
    left: 676px; width: 196px; top: 628px; color: var(--red); font-family: "Anton", sans-serif;
    font-size: 94px; line-height: 82px; text-align: center; transform: skewX(-8deg);
  }
  .contact {
    left: 14px; width: 290px; top: 842px; text-align: center; color: var(--white);
    font-size: 22px; line-height: 30px;
  }
  .contact-web {
    left: 14px; width: 290px; top: 938px; text-align: center; color: var(--white);
    font-family: "Oswald", sans-serif; font-weight: 700; font-size: 25px; line-height: 1.2;
  }
  .join {
    left: 32px; top: 1004px; color: var(--red); font-family: "Anton", sans-serif;
    font-size: 50px; line-height: 1; transform: rotate(-14deg); transform-origin: left bottom;
  }
</style>
</head>
<body>
<main class="flyer">
  <svg class="art" width="927" height="1200" viewBox="0 0 927 1200">
    <defs>
      <radialGradient id="stage-glow" cx="0.55" cy="0.45" r="0.75">
        <stop offset="0" stop-color="#2a46b8"/>
        <stop offset="0.6" stop-color="#1f36a0"/>
        <stop offset="1" stop-color="#0d1a5c"/>
      </radialGradient>
      <linearGradient id="skate-tones" x1="0" y1="0" x2="0" y2="1">
        <stop offset="0" stop-color="#1b1b1b"/>
        <stop offset="0.55" stop-color="#3a3a3a"/>
        <stop offset="1" stop-color="#9a9a9a"/>
      </linearGradient>
      <linearGradient id="photo-warm" x1="0" y1="0" x2="1" y2="1">
        <stop offset="0" stop-color="#5a6fc0"/>
        <stop offset="1" stop-color="#c9a48a"/>
      </linearGradient>
      <linearGradient id="photo-cool" x1="0" y1="0" x2="1" y2="1">
        <stop offset="0" stop-color="#3b3f8a"/>
        <stop offset="1" stop-color="#b8c2d8"/>
      </linearGradient>
    </defs>

    <rect class="backdrop" x="0" y="0" width="927" height="983" fill="url(#stage-glow)"/>
    <rect class="print-space" x="0" y="983" width="927" height="217" fill="#ffffff"/>

    <circle class="title-disc" cx="338" cy="441" r="324" fill="#ffffff"/>

    <path class="bunting-string" d="M0 165 Q300 90 560 10" stroke="#333" stroke-width="1.5" fill="none"/>
    <polygon class="pennant" points="36,152 193,122 150,330" fill="#e41e26"/>
    <polygon class="pennant" points="222,116 372,74 349,285" fill="#f7c21b"/>
    <polygon class="pennant" points="400,70 551,8 548,218" fill="#19b6ef"/>

    <rect class="skate-art" x="530" y="0" width="397" height="375" fill="url(#skate-tones)" role="img" aria-label="Illustration of a black roller skate with white laces and grey wheels"/>

    <path class="night-swoosh" d="M406 503 Q520 472 637 480 Q540 485 406 503 Z" fill="#111111" stroke="#111111" stroke-width="3"/>

    <circle class="brand-mark" cx="774" cy="489" r="90" fill="#1f36a0" stroke="#ffffff" stroke-width="4"/>

    <path class="photo-string" d="M0 513 Q420 770 927 826" stroke="#555" stroke-width="2" fill="none"/>

    <polygon class="photo-pennant" points="22,535 244,642 11,843" fill="url(#photo-cool)" stroke="#ffffff" stroke-width="3" role="img" aria-label="Photo of a child roller skating with a glow necklace"/>
    <polygon class="photo-pennant" points="288,662 500,752 302,966" fill="url(#photo-warm)" stroke="#ffffff" stroke-width="3" role="img" aria-label="Photo of a smiling boy in the play zone"/>
    <polygon class="photo-pennant" points="513,749 741,807 560,1054" fill="url(#photo-cool)" stroke="#ffffff" stroke-width="3" role="img" aria-label="Photo of three girls hugging at the rink"/>
    <polygon class="photo-pennant" points="747,807 927,824 927,980 838,1104" fill="url(#photo-warm)" stroke="#ffffff" stroke-width="3" role="img" aria-label="Photo of a mother and two girls skating together"/>
  </svg>

  <p class="text tagline">FAMILY FUN, ENTERTAINMENT!</p>

  <h1 class="text title-script">Skate</h1>
  <p class="text title-night">NIGHT</p>

  <p class="text prices prices--single">$6 Skate &#9670; $6 Play Zone</p>
  <p class="text prices prices--bundle">$10 Skate &amp; Play Bundle!</p>
  <p class="text price-note">Prices per person.<br>Skate rental included!</p>

  <p class="text brand-name">MAPLEWOOD SKATE CENTER</p>

  <p class="text promo-lead">Don’t miss the</p>
  <p class="text promo-main">PLAY<br>ZONE!</p>

  <p class="text contact">847 S. Pinecrest Ave.<br>Wichita, KS 67219<br>Ph.&nbsp; (316) 555-0187</p>
  <p class="text contact-web">www.maplewheelrink.com</p>

  <p class="text join">JOIN US!</p>
</main>
</body>
</html>
```